Simple menu needed for Asian food truck

We are an Asian food truck that attends big festivals. Our menu is very simple featuring only about 5 or 6 dishes, but we need big pictures and lettering to capture the attention of festival goers. Our motto is "Fresh, Authentic, Homemade", it would be great to include that somewhere. We also need a menu that possibly magnetic so that we can easily take off items that are sold out, change pricing or add different dishes for specific venues. Attached is an example of what our current menu looks like.

```html
<!DOCTYPE html>
<html lang="en">
<head>
<meta charset="UTF-8">
<title>Kiri's Egg Rolls – Festival Menu</title>
<link rel="stylesheet" href="https://fonts.googleapis.com/css2?family=Oswald:wght@500;600&family=Montserrat:wght@500;800&display=swap">
<style>
  :root {
    --orange: #d9802a;
    --orange-deep: #c96f1e;
    --black: #1a1918;
    --black-soft: #272523;
    --yellow: #f9c846;
    --yellow-bright: #fbd447;
    --white: #ffffff;
    --ink: #1b1b1b;
  }
  * { margin: 0; padding: 0; box-sizing: border-box; }
  html, body { width: 950px; height: 1200px; overflow: hidden; background: var(--black); }
  .menu {
    position: relative; width: 950px; height: 1200px; overflow: hidden;
    background: var(--orange);
    font-family: 'Montserrat', sans-serif;
  }
  .menu__backdrop { position: absolute; inset: 0; }

  .brand-ribbon {
    position: absolute; left: 68px; top: 0; width: 182px; height: 266px;
    background: var(--white);
    clip-path: polygon(0 0, 100% 0, 100% 100%, 50% 84%, 0 100%);
    display: flex; flex-direction: column; align-items: center; padding-top: 52px;
  }
  .brand-ribbon__mark {
    width: 120px; height: 120px; border-radius: 50%;
    border: 3px solid var(--orange);
    display: flex; align-items: center; justify-content: center; text-align: center;
  }
  .brand-ribbon__name {
    font-family: 'Oswald', sans-serif; font-weight: 600; color: var(--orange);
    font-size: 30px; line-height: 1; text-transform: uppercase;
  }

  .motto-ring { position: absolute; left: 540px; top: 40px; }
  .motto {
    position: absolute; right: 40px; top: 118px; width: 300px;
    font-family: 'Oswald', sans-serif; font-weight: 600; color: var(--yellow-bright);
    font-size: 68px; line-height: 87px; text-align: center; text-transform: uppercase;
  }

  .menu-item { position: absolute; width: 220px; text-align: center; }
  .menu-item__photo {
    margin: 0 auto; height: 100px; border-radius: 10px 40px 10px 40px;
    background: linear-gradient(160deg, #f4f1ea 0%, #e4c07a 45%, #b8732d 100%);
    box-shadow: 0 6px 12px rgba(0,0,0,.4);
  }
  .menu-item__badge {
    width: 200px; height: 200px; margin: -8px auto 0; border-radius: 50%;
    background: var(--yellow); border: 6px solid var(--orange-deep);
    box-shadow: 0 8px 16px rgba(0,0,0,.45);
    display: flex; flex-direction: column; align-items: center; justify-content: center;
    padding: 0 14px;
  }
  .menu-item__name { font-weight: 800; font-size: 21px; line-height: 1.1; color: var(--ink); text-transform: uppercase; }
  .menu-item__note { font-weight: 500; font-size: 11.5px; line-height: 1.25; color: var(--ink); }
  .menu-item__price {
    font-family: 'Oswald', sans-serif; font-weight: 500; font-size: 34px;
    color: var(--orange-deep); margin-top: 4px; line-height: 1.1; text-transform: uppercase;
  }

  .item--eggrolls { left: 82px; top: 353px; }
  .item--springrolls { left: 371px; top: 364px; }
  .item--bbq { left: 652px; top: 553px; }
  .item--rice { left: 49px; top: 697px; }
  .item--wing { left: 342px; top: 706px; }
  .item--eggrolls .menu-item__photo { width: 210px; height: 120px; }
  .item--springrolls .menu-item__photo { width: 215px; background: linear-gradient(160deg, #f6f4f0, #dfe8dc 50%, #f0a88e); }
  .item--bbq .menu-item__photo { width: 215px; background: linear-gradient(160deg, #f5f3ef, #8d2738 55%, #5a1620); }
  .item--rice .menu-item__photo { width: 215px; background: linear-gradient(160deg, #f5f3ef, #d7b57a 50%, #a4552d); }
  .item--wing .menu-item__photo { width: 228px; height: 78px; margin-bottom: 14px; }

  .tea-photo {
    position: absolute; left: 577px; top: 886px; width: 272px; height: 200px;
    border-radius: 12px;
    background: linear-gradient(90deg, #ec6a4e 0%, #f48e52 30%, #f9c132 55%, #f2d36a 100%);
  }
  .tea-banner { position: absolute; left: 474px; top: 1066px; width: 476px; height: 110px; }
  .tea-banner__text { position: absolute; inset: 0; text-align: center; padding-top: 12px; }
  .tea-banner__title { font-family: 'Oswald', sans-serif; font-weight: 600; font-size: 44px; line-height: 1; color: var(--ink); text-transform: uppercase; }
  .tea-banner__flavors { font-family: 'Oswald', sans-serif; font-weight: 500; font-size: 23px; color: var(--orange-deep); text-transform: uppercase; margin-top: 6px; }

  .payments {
    position: absolute; left: 78px; top: 1036px;
    display: grid; grid-template-columns: 97px 97px; gap: 8px;
  }
  .payments__card { height: 58px; border-radius: 6px; box-shadow: 0 3px 6px rgba(0,0,0,.5); }
  .payments__card--light { background: linear-gradient(#ffffff, #dcdcdc); }
  .payments__card--blue { background: linear-gradient(#5d8fd6, #3b6fb8); }
  .payments__card--split { background: linear-gradient(160deg, #ffffff 55%, #ef7d22 55%); }
</style>
</head>
<body>
<main class="menu">
  <svg class="menu__backdrop" width="950" height="1200" viewBox="0 0 950 1200" aria-hidden="true">
    <defs>
      <radialGradient id="board" cx="50%" cy="55%" r="70%">
        <stop offset="0" stop-color="#2a2826"/>
        <stop offset="1" stop-color="#151413"/>
      </radialGradient>
    </defs>
    <path fill="url(#board)" d="M0,285 C60,250 110,215 170,200 C250,180 290,140 340,110 C400,75 450,95 500,80 C560,62 600,120 650,110 C700,100 720,40 770,45 C800,50 800,110 825,110 C845,110 845,40 870,38 C900,36 905,110 920,200 C928,240 940,255 950,255 L950,1200 L0,1200 Z"/>
  </svg>

  <div class="brand-ribbon">
    <div class="brand-ribbon__mark"><span class="brand-ribbon__name">Kiri's<br>Egg Rolls</span></div>
  </div>

  <svg class="motto-ring" width="410" height="410" viewBox="0 0 410 410" aria-hidden="true">
    <circle cx="205" cy="205" r="196" fill="none" stroke="#c9a24a" stroke-width="3" opacity=".85"/>
    <circle cx="208" cy="202" r="188" fill="none" stroke="#c9a24a" stroke-width="1.5" opacity=".5"/>
  </svg>
  <h1 class="motto">Fresh,<br>Authentic,<br>Homemade</h1>

  <section class="menu-item item--eggrolls">
    <div class="menu-item__photo" role="img" aria-label="Photo of three chicken egg rolls in a paper tray"></div>
    <div class="menu-item__badge">
      <h2 class="menu-item__name">Chicken<br>Eggrolls</h2>
      <p class="menu-item__price">3 for $6</p>
    </div>
  </section>

  <section class="menu-item item--springrolls">
    <div class="menu-item__photo" role="img" aria-label="Photo of fresh shrimp spring rolls in a paper tray"></div>
    <div class="menu-item__badge">
      <h2 class="menu-item__name">Fresh<br>Springrolls</h2>
      <p class="menu-item__note">(Shrimp or Veggie)</p>
      <p class="menu-item__price">2 for $6</p>
    </div>
  </section>

  <section class="menu-item item--bbq">
    <div class="menu-item__photo" role="img" aria-label="Photo of Chinese BBQ skewers in a paper tray"></div>
    <div class="menu-item__badge">
      <h2 class="menu-item__name">Chinese BBQ<br>Skewers</h2>
      <p class="menu-item__price">2 for $6</p>
    </div>
  </section>

  <section class="menu-item item--rice">
    <div class="menu-item__photo" role="img" aria-label="Photo of fried rice in a paper tray"></div>
    <div class="menu-item__badge">
      <h2 class="menu-item__name">Fries Rice</h2>
      <p class="menu-item__note">(Chicenn or &nbsp;Pork)</p>
      <p class="menu-item__price">$5 Bowl</p>
    </div>
  </section>

  <section class="menu-item item--wing">
    <div class="menu-item__photo" role="img" aria-label="Photo of a stuffed chicken wing with fried rice in a paper tray"></div>
    <div class="menu-item__badge">
      <h2 class="menu-item__name">Angel Wing</h2>
      <p class="menu-item__note">(Stuffed Chiecken Wing)<br>with side of fried rice</p>
      <p class="menu-item__price">$8 Combo</p>
    </div>
  </section>

  <div class="tea-photo" role="img" aria-label="Photo of three iced flavored teas: strawberry, mango and peach"></div>
  <div class="tea-banner">
    <svg width="476" height="110" viewBox="0 0 476 110" aria-hidden="true">
      <path fill="#f7c33e" d="M40,8 L470,4 L460,30 L476,48 L455,62 L470,82 L420,96 L430,108 L30,106 L50,92 L0,84 L36,70 L10,52 L48,40 L20,22 Z"/>
    </svg>
    <div class="tea-banner__text">
      <p class="tea-banner__title">Flavored Tea $5,</p>
      <p class="tea-banner__flavors">Strawberry, Mango, Peach</p>
    </div>
  </div>

  <div class="payments" aria-label="Accepted payment cards">
    <div class="payments__card payments__card--light"></div>
    <div class="payments__card payments__card--blue"></div>
    <div class="payments__card payments__card--split"></div>
    <div class="payments__card payments__card--blue"></div>
  </div>
</main>
</body>
</html>
```